Business Card for beauty technology startup

Design Glowmi Business Card for a Beauty, based on the website identity and colors (https://www.glowmi-example.com).
Glowmi is a beauty tech startup that gathers helpful product info for beauty lovers and consumers (such as availability on stores, price range and product reviews) for makeup products. The card design must be young, colorful but clean, and very modern.

Target Market(s)

woman, 15-35

Industry/Entity Type

Cosmetics

Contact Information for Business Card

Full Name, address, phone

Font styles to use
Other font styles liked:
• Advent Pro

Colors
e34297
86cfc6
ffffff
5c5c5c
e8e8e8
e667a6
b2b2b2

Requirements
Must have
• One full colored side with a creative design and another with card info
• Use Color palette: #95C5C5 and/or #D38AA5
• Use fonts: Advent Pro
• Use website identity: https://www.glowmi-example.com
Nice to have
• If needed extra font: Roboto

```html
<!DOCTYPE html>
<html lang="en">
<head>
<meta charset="utf-8">
<title>Glowmi Business Card</title>
<link rel="stylesheet" href="https://fonts.googleapis.com/css2?family=Advent+Pro:wght@200;300;400;700&family=Roboto:wght@500;700&display=swap">
<style>
  :root {
    --stage: #141414;
    --teal: #86cfc6;
    --teal-deep: #79c2b9;
    --white: #ffffff;
    --ink: #1e1a1a;
    --soft-ink: #3a3434;
  }
  * { box-sizing: border-box; margin: 0; padding: 0; }
  html, body {
    width: 1200px; height: 1200px; overflow: hidden;
    background: var(--stage);
  }
  .stage { position: relative; width: 1200px; height: 1200px; }
  .card {
    position: absolute; left: 220px; width: 760px; height: 430px;
    overflow: hidden; border-radius: 3px;
    box-shadow: 0 18px 40px rgba(0,0,0,.55);
  }
  .card-front { top: 110px; background: var(--teal); }
  .card-back { top: 640px; background: var(--white); }
  .card svg.card-art { position: absolute; inset: 0; }

  .front-ring {
    position: absolute; left: 270px; top: 90px; width: 220px; height: 220px;
    border-radius: 50%; border: 14px solid var(--teal-deep);
  }
  .front-wordmark {
    position: absolute; left: 0; right: 0; top: 130px; text-align: center;
    font-family: "Advent Pro", sans-serif; font-weight: 200;
    font-size: 118px; letter-spacing: 14px; color: var(--white);
  }
  .front-url {
    position: absolute; left: 0; right: 0; top: 340px; text-align: center;
    font-family: "Roboto", sans-serif; font-weight: 700;
    font-size: 22px; letter-spacing: 2.5px; color: var(--white);
  }

  .brand { position: absolute; left: 150px; top: 52px; display: flex; align-items: center; gap: 26px; }
  .brand-dot { width: 86px; height: 86px; border-radius: 50%; border: 3px solid var(--ink); }
  .brand-name {
    font-family: "Advent Pro", sans-serif; font-weight: 300;
    font-size: 72px; letter-spacing: 9px; color: var(--ink); line-height: 1;
  }
  .holder { position: absolute; left: 300px; top: 162px; text-align: center; }
  .holder-name {
    font-family: "Advent Pro", sans-serif; font-weight: 700;
    font-size: 42px; color: var(--ink); line-height: 1; letter-spacing: .5px;
  }
  .holder-role {
    font-family: "Advent Pro", sans-serif; font-weight: 300;
    font-size: 24px; color: var(--soft-ink); line-height: 1.1;
  }
  .contact {
    position: absolute; top: 352px;
    font-family: "Advent Pro", sans-serif; font-weight: 400;
    font-size: 24px; line-height: 30px; color: var(--white);
  }
  .contact-reach { right: 330px; text-align: right; }
  .contact-place { left: 470px; }
  .contact-divider {
    position: absolute; left: 450px; top: 352px; width: 1px; height: 62px;
    background: rgba(255,255,255,.7);
  }
  .icon { position: absolute; }
</style>
</head>
<body>
<main class="stage">

  <section class="card card-front" aria-label="Card front">
    <div class="front-ring"></div>
    <div class="front-wordmark">GLOWMI</div>
    <div class="front-url">www.glowmi-example.com</div>
  </section>

  <section class="card card-back" aria-label="Card back">
    <svg class="card-art" width="760" height="430" viewBox="0 0 760 430">
      <path d="M0 310 C280 310 560 250 760 150 V430 H0 Z" fill="var(--teal)"/>
      <path d="M0 330 C290 330 570 268 760 166 V186 C570 288 290 356 0 356 Z" fill="var(--white)"/>
      <path d="M0 310 C280 310 560 250 760 150" fill="none" stroke="var(--ink)" stroke-width="4"/>
    </svg>

    <div class="brand">
      <span class="brand-dot"></span>
      <span class="brand-name">GLOWMI</span>
    </div>
    <div class="holder">
      <div class="holder-name">JOHN DOE</div>
      <div class="holder-role">Director</div>
    </div>

    <div class="contact contact-reach">
      <div>1-234-567890</div>
      <div>www.glowmi-example.com</div>
    </div>
    <svg class="icon" style="left:438px;top:357px" width="20" height="20" viewBox="0 0 20 20" aria-hidden="true">
      <path d="M3 8 C3 3 17 3 17 8 L14 9 L13 7 C11 6 9 6 7 7 L6 9 Z M5 11 H15 L16 17 H4 Z" fill="var(--soft-ink)"/>
    </svg>
    <svg class="icon" style="left:438px;top:388px" width="20" height="20" viewBox="0 0 20 20" aria-hidden="true">
      <circle cx="10" cy="10" r="8" fill="none" stroke="var(--soft-ink)" stroke-width="2"/>
      <path d="M2 10 H18 M10 2 C6 6 6 14 10 18 M10 2 C14 6 14 14 10 18" fill="none" stroke="var(--soft-ink)" stroke-width="1.5"/>
    </svg>
    <div class="contact-divider"></div>
    <svg class="icon" style="left:462px;top:356px" width="16" height="22" viewBox="0 0 16 22" aria-hidden="true">
      <path d="M8 0 C3.6 0 0 3.4 0 7.6 C0 13 8 22 8 22 S16 13 16 7.6 C16 3.4 12.4 0 8 0 Z M8 4.5 A3 3 0 1 1 8 10.5 A3 3 0 1 1 8 4.5 Z" fill="var(--soft-ink)"/>
    </svg>
    <div class="contact contact-place" style="left:486px">
      <div>Dummy city</div>
      <div>Dummy Country Land</div>
    </div>
  </section>

</main>
</body>
</html>
```